Illustrations for a Project Management Concept

we need illustrations for 5 project management principles that make up a holistic approach to project management, without all the BS. if we extract all the methodology, system, tool and mumbo-jumbo out of project management, we end up with some essential principles that are simple to understand and use. It's likely that people who use them will not be traditional Project Management types.

I've mocked up something that looks very corporate based on a template, but this has the wrong tone; the wrong feeling. I'd like something "funky" and colorful that conveys "Action" within "Simplicity".

the PPT file with the dark-blue background is the "corporate" consulting type mockup. the PPT with the white background shows an idea I had for breaking out each of the 5 principles (only one shown) to make it larger, with some text in a callout.

In the final deliverable, I need to be able to both show all 5 on one diagram, as well as slicing the image to display each principle separately. i do not have editing capabilities for vector image formats, only image formats

Reason: there are a number of designers who have only just accepted the invitation. I want to give everyone a chance to submit.

```html
<!DOCTYPE html>
<html lang="en">
<head>
<meta charset="utf-8">
<title>5 Project Action Principles</title>
<link rel="stylesheet" href="https://fonts.googleapis.com/css2?family=Bebas+Neue&family=Open+Sans:wght@400&display=swap">
<style>
  :root {
    --purple: #5a17c9;
    --purple-dark: #3e0a9a;
    --red: #d01616;
    --red-dark: #9c0c0c;
    --orange: #d96f12;
    --orange-dark: #a84f06;
    --blue: #1a4fd0;
    --blue-dark: #0c2f92;
    --heading-blue: #1b3f9e;
    --hub-grey: #777777;
    --body-grey: #7a7a7a;
    --paper: #ffffff;
  }
  html, body { margin: 0; padding: 0; width: 1200px; height: 764px; overflow: hidden; background: var(--paper); }
  .canvas { position: relative; width: 1200px; height: 764px; overflow: hidden; background: var(--paper); }
  .diagram { position: absolute; left: 0; top: 0; width: 1200px; height: 764px; display: block; }
  .ring-label { font-family: "Bebas Neue", "Oswald", sans-serif; font-size: 34px; fill: #fff; }
  .hub-label { font-family: "Bebas Neue", "Oswald", sans-serif; font-size: 62px; fill: var(--hub-grey); }
  .summary { position: absolute; left: 780px; top: 172px; width: 330px; }
  .summary-title {
    margin: 0; font-family: "Bebas Neue", "Oswald", sans-serif; font-weight: 400;
    font-size: 30px; line-height: 28px; letter-spacing: 0.8px; color: var(--heading-blue);
  }
  .summary-rule { width: 295px; height: 2px; background: var(--red); border: 0; margin: 0; }
  .summary-rule.top { margin-top: 20px; }
  .summary-text {
    margin: 14px 0 18px; font-family: "Open Sans", Arial, sans-serif; font-size: 17px;
    line-height: 22.4px; color: var(--body-grey);
  }
  .summary-text .lead { color: var(--red); }
</style>
</head>
<body>
<div class="canvas">
  <svg class="diagram" viewBox="0 0 1100 700" aria-label="Five project action principles around achieving outcomes">
    <defs>
      <filter id="soft-shadow" x="-30%" y="-30%" width="160%" height="160%">
        <feDropShadow dx="0" dy="4" stdDeviation="9" flood-color="#000" flood-opacity="0.18"/>
      </filter>
      <linearGradient id="grad-purple" x1="0" y1="0" x2="0" y2="1"><stop offset="0" stop-color="#5a17c9"/><stop offset="1" stop-color="#3e0a9a"/></linearGradient>
      <linearGradient id="grad-red" x1="1" y1="0" x2="0" y2="0"><stop offset="0" stop-color="#9c0c0c"/><stop offset="0.6" stop-color="#d01616"/></linearGradient>
      <linearGradient id="grad-orange" x1="0" y1="0" x2="1" y2="0"><stop offset="0" stop-color="#a84f06"/><stop offset="0.6" stop-color="#d96f12"/></linearGradient>
      <linearGradient id="grad-blue" x1="0" y1="1" x2="0" y2="0"><stop offset="0" stop-color="#0c2f92"/><stop offset="0.6" stop-color="#1a4fd0"/></linearGradient>
      <path id="arc-top" d="M202.3 245.5 A219 219 0 0 1 581.7 245.5"/>
      <path id="arc-bottom" d="M181.6 476.5 A243 243 0 0 0 602.4 476.5"/>
      <path id="segment" d="M230.7 148.5 A262 262 0 0 1 553.3 148.5 L515.1 197.4 A200 200 0 0 0 268.9 197.4 Z"/>
    </defs>

    <polygon class="corner corner-top" points="0,0 125,0 0,58" fill="var(--purple)"/>
    <polygon class="corner corner-bottom" points="1100,636 1100,700 970,700" fill="var(--orange)"/>

    <g class="cross-bands" filter="url(#soft-shadow)">
      <rect x="92" y="320" width="600" height="70" fill="var(--paper)" transform="rotate(45 392 355)"/>
      <rect x="92" y="320" width="600" height="70" fill="var(--paper)" transform="rotate(-45 392 355)"/>
    </g>

    <g class="segments" filter="url(#soft-shadow)">
      <use href="#segment" fill="url(#grad-purple)"/>
      <use href="#segment" fill="url(#grad-red)" transform="rotate(90 392 355)"/>
      <use href="#segment" fill="url(#grad-blue)" transform="rotate(180 392 355)"/>
      <use href="#segment" fill="url(#grad-orange)" transform="rotate(-90 392 355)"/>
    </g>

    <g class="labels">
      <text class="ring-label"><textPath href="#arc-top" startOffset="50%" text-anchor="middle" textLength="285" lengthAdjust="spacingAndGlyphs">FULFIL CUSTOMER VALUE</textPath></text>
      <g transform="rotate(90 392 355)"><text class="ring-label"><textPath href="#arc-top" startOffset="50%" text-anchor="middle" textLength="262" lengthAdjust="spacingAndGlyphs">BUILD SHARED MODELS</textPath></text></g>
      <g transform="rotate(-90 392 355)"><text class="ring-label"><textPath href="#arc-top" startOffset="50%" text-anchor="middle" textLength="285" lengthAdjust="spacingAndGlyphs">ELIMINATE TEAMING THREATS</textPath></text></g>
      <text class="ring-label"><textPath href="#arc-bottom" startOffset="50%" text-anchor="middle" textLength="220" lengthAdjust="spacingAndGlyphs">SUPPRESS ENTROPY</textPath></text>
    </g>

    <g class="hub">
      <polyline points="377,214 392,201 407,214" fill="none" stroke="var(--purple)" stroke-width="3"/>
      <polyline points="541,336 553,350 541,364" fill="none" stroke="var(--red)" stroke-width="3"/>
      <polyline points="377,488 392,501 407,488" fill="none" stroke="var(--blue)" stroke-width="3"/>
      <polyline points="245,336 232,350 245,364" fill="none" stroke="var(--orange)" stroke-width="3"/>
      <text class="hub-label" x="392" y="346" text-anchor="middle">ACHIEVE</text>
      <text class="hub-label" x="392" y="396" text-anchor="middle">OUTCOMES</text>
    </g>
  </svg>

  <div class="summary">
    <h1 class="summary-title">5 Project Action Principles<br>for Successful Project<br>Management</h1>
    <hr class="summary-rule top">
    <p class="summary-text"><span class="lead">The Five Project Action</span> Principles<br>a set of higher-order principles<br>that stand outside day-to-day<br>processes we may use,<br>and which guide people to align<br>productively around a clear<br>end-goal and determine a delivery<br>approach.</p>
    <hr class="summary-rule">
  </div>
</div>
</body>
</html>
```